brindle's business card for earthmoving and tipper hire business.

I have a small earthmoving and tipper truck company. I am aiming for the smaller jobs that the big guys don't want. I am also Doing grass slashing and fire hazard reduction work. I would like to see some earthy colors, greens browns etc. I have a tractor with a front end loader attachment, and a 22 ton tipper. I would like to maybe have a silhouette of a tipper and tractor/slasher/loader setup in centre with my business name over the top and details to one side or something like that

Industry/Entity Type

Business

Contact Information for Business Card

Brindle's small earthworks and tipper hireToowoombaABN: 47781050480PH 0479126773Email brindle.4@fenwickmail.com

Font styles to use
Sans Serif

Colors
fbee3d
abd036
85cae6
f78f20

Requirements
Nice to have
• Earthy colors . business name in blue

```html
<!DOCTYPE html>
<html lang="en">
<head>
<meta charset="utf-8">
<title>Brindle's Small Earthworks – Business Card</title>
<link href="https://fonts.googleapis.com/css2?family=Montserrat:wght@800&family=Roboto+Condensed:wght@700&family=Source+Sans+3:wght@600;700&display=swap" rel="stylesheet">
<style>
  :root {
    --card-yellow: #f9ed3e;
    --card-yellow-deep: #eedf34;
    --sky-blue: #85cae6;
    --leaf-green: #abd036;
    --earth-orange: #f78f20;
    --page: #ffffff;
  }
  html, body {
    margin: 0;
    padding: 0;
    width: 1200px;
    height: 1000px;
    overflow: hidden;
    background: var(--page);
  }
  .canvas {
    position: relative;
    width: 1200px;
    height: 1000px;
  }
  .card {
    position: absolute;
    left: 63px;
    top: 175px;
    width: 1074px;
    height: 650px;
    background: var(--card-yellow);
    overflow: hidden;
  }
  .backdrop-machinery {
    position: absolute;
    left: 0;
    top: 0;
    width: 1074px;
    height: 520px;
    display: block;
  }
  .business-name {
    position: absolute;
    left: 0;
    width: 100%;
    top: 62px;
    margin: 0;
    text-align: center;
    font-family: "Montserrat", sans-serif;
    font-weight: 800;
    font-size: 47px;
    letter-spacing: 2px;
    color: var(--sky-blue);
    line-height: 1;
  }
  .business-sub {
    position: absolute;
    left: 0;
    width: 100%;
    top: 128px;
    margin: 0;
    text-align: center;
    font-family: "Roboto Condensed", sans-serif;
    font-weight: 700;
    font-size: 37px;
    color: var(--sky-blue);
    text-shadow: 2px 2px 0 rgba(0,0,0,0.12);
    line-height: 1;
  }
  .hero-machines {
    position: absolute;
    left: 107px;
    top: 160px;
    width: 870px;
    height: 270px;
    display: block;
  }
  .contact-list {
    position: absolute;
    left: 50px;
    top: 480px;
    margin: 0;
    font-family: "Source Sans 3", sans-serif;
    font-weight: 700;
    font-size: 33px;
    color: var(--earth-orange);
    line-height: 45px;
  }
  .contact-row { display: flex; }
  .contact-label { width: 106px; }
  .services {
    position: absolute;
    right: 84px;
    top: 432px;
    margin: 0;
    padding: 0;
    list-style: none;
    text-align: right;
    font-family: "Source Sans 3", sans-serif;
    font-weight: 700;
    font-size: 25px;
    color: var(--leaf-green);
    line-height: 35.5px;
  }
  .services li::after {
    content: "•";
    margin-left: 4px;
  }
  .services-tag {
    position: absolute;
    left: 1000px;
    top: 437px;
    margin: 0;
    writing-mode: vertical-rl;
    font-family: "Source Sans 3", sans-serif;
    font-weight: 700;
    font-size: 25px;
    letter-spacing: 1px;
    color: var(--earth-orange);
    line-height: 1;
  }
</style>
</head>
<body>
<div class="canvas">
  <section class="card">
    <svg class="backdrop-machinery" viewBox="0 0 1074 520" role="img" aria-label="Faint enlarged tractor and tipper truck illustration in the background">
      <defs>
        <linearGradient id="faintTone" x1="0" y1="0" x2="1" y2="0">
          <stop offset="0" stop-color="var(--card-yellow-deep)" stop-opacity="0.9"/>
          <stop offset="0.5" stop-color="var(--card-yellow-deep)" stop-opacity="0.35"/>
          <stop offset="1" stop-color="var(--card-yellow-deep)" stop-opacity="0.9"/>
        </linearGradient>
      </defs>
      <rect x="0" y="110" width="1074" height="410" fill="url(#faintTone)"/>
    </svg>

    <h1 class="business-name">BRINDLE'S SMALL EARTHWORKS</h1>
    <p class="business-sub">AND TIPPER HIRETOOWOOMBA</p>

    <svg class="hero-machines" viewBox="0 0 870 270" role="img" aria-label="Orange line illustration of a tractor and a tipper truck tipping its load">
      <rect x="0" y="40" width="400" height="230" rx="20" fill="var(--earth-orange)"/>
      <rect x="420" y="0" width="450" height="270" rx="20" fill="var(--earth-orange)"/>
    </svg>

    <div class="contact-list">
      <div class="contact-row"><span class="contact-label">ABN</span><span>: 62194038715</span></div>
      <div class="contact-row"><span class="contact-label">PH</span><span>: 0438571629</span></div>
      <div class="contact-row"><span class="contact-label">Email</span><span>: brindle.4@fenwickmail.com</span></div>
    </div>

    <ul class="services">
      <li>SMALL EARTHWORKS</li>
      <li>SLASHING</li>
      <li>Five Hazard Reduction</li>
      <li>Rural Cleanups</li>
      <li>Tipper</li>
    </ul>
    <p class="services-tag">DOT POINTS</p>
  </section>
</div>
</body>
</html>
```